Business card design for new brand

We have recently rebranded and need a new business card template.

We are an insurance underwriting agency. All of our products are sold via other partner companies, so these are just to pass on our details to other organisations.

We would like to see designs that use the colour green (current stationary generally uses lime green (rgb 142,190,63) and forest green (0,154,79) to comply with our logo's colours. We are happy with other shades of green.

Business cards need to include our logo, as well as space for:
1. Full name
2. Qualifications (optional)
3. Title
4. Office number
5. Mobile number
6. Email address

Our logo is enclosed here.

```html
<!DOCTYPE html>
<html lang="en">
<head>
<meta charset="utf-8">
<title>Greenvale Underwriting – Business Card</title>
<link rel="stylesheet" href="https://fonts.googleapis.com/css2?family=Ubuntu:wght@300;400;500;700&display=swap">
<style>
  :root {
    --backdrop: #2a2d30;
    --card-dark: #0d0d0d;
    --card-light: #f1f2f2;
    --ink-dark: #1c1c1c;
    --ink-light: #f2f2f2;
    --lime: #8ebe3f;
    --forest: #009a4f;
  }
  * { margin: 0; padding: 0; box-sizing: border-box; }
  html, body { width: 1200px; height: 780px; overflow: hidden; }
  body {
    background: var(--backdrop);
    font-family: "Ubuntu", sans-serif;
    position: relative;
  }
  .card {
    position: absolute;
    width: 500px;
    height: 306px;
    border-radius: 4px;
    box-shadow: 0 14px 30px rgba(0,0,0,0.45);
  }
  /* Back: contact details */
  .card-back {
    left: 60px; top: 237px;
    background: var(--card-dark);
    color: var(--ink-light);
    padding: 38px 40px;
  }
  .person-name {
    color: var(--lime);
    font-weight: 700;
    font-size: 21px;
    letter-spacing: 0.5px;
    text-transform: uppercase;
  }
  .person-title {
    font-size: 14px;
    font-weight: 300;
    margin-top: 4px;
  }
  .name-rule {
    width: 30px; height: 2px;
    background: var(--lime);
    margin: 22px 0 22px;
  }
  .contact-list { list-style: none; font-size: 13px; line-height: 1.55; font-weight: 300; }
  .contact-label { color: var(--lime); }
  .back-brand {
    position: absolute;
    right: 34px; bottom: 30px;
    display: flex; align-items: center; gap: 8px;
    font-size: 16px; font-weight: 500; color: var(--ink-light);
  }
  .brand-square {
    width: 14px; height: 14px;
    background: var(--forest);
  }
  /* Front: brand face */
  .card-front {
    left: 640px; top: 237px;
    background: var(--card-light);
    color: var(--ink-dark);
    display: flex; flex-direction: column; align-items: center; justify-content: center;
  }
  .front-brand { display: flex; align-items: center; gap: 14px; }
  .front-brand .brand-square { width: 34px; height: 34px; }
  .brand-name { font-size: 44px; font-weight: 500; line-height: 1; }
  .brand-sub { font-size: 16px; font-weight: 300; margin-top: 4px; text-align: right; }
  .brand-web {
    margin-top: 30px;
    font-size: 12px;
    letter-spacing: 2.4px;
    text-transform: uppercase;
  }
</style>
</head>
<body>
  <section class="card card-back" aria-label="Business card back">
    <h1 class="person-name">Marcus Hale</h1>
    <p class="person-title">Account manager</p>
    <div class="name-rule"></div>
    <ul class="contact-list">
      <li><span class="contact-label">Office:</span> 0100 200 3000</li>
      <li><span class="contact-label">Mob:</span> 0400 111 222</li>
      <li>hello@greenvalecover.com.au</li>
      <li>www.greenvalecover.com.au</li>
    </ul>
    <div class="back-brand"><span class="brand-square"></span>Greenvale</div>
  </section>

  <section class="card card-front" aria-label="Business card front">
    <div class="front-brand">
      <span class="brand-square"></span>
      <div>
        <div class="brand-name">Greenvale</div>
        <div class="brand-sub">Underwriting Pty Ltd</div>
      </div>
    </div>
    <p class="brand-web">www.greenvalecover.com.au</p>
  </section>
</body>
</html>
```